40k Ultra High Pressure Waterblasting Ad

Clean, Simple, To the point. We need an ad for our industry magazine. Our company Brightwell Spraytek Systems, Inc. caters to contractors in the Utra High Pressure Waterblasting Industry. We manufacture in house a majority of the items we sell. We'd like the ad to imply that we believe in good customer service, building relationships with our customers and going above and beyond to meet our customer needs. Our main products we sell are our Quillstone Nozzles and Dorvane Mellick Hoses. Our website is Brightwellspraytek.example for images of our products.

Attached are some of our previous ads we've made.

I like the icons we used in the "Dorvane ad" listing some of our keys products we sell.

Target Market(s)

Contractors

Industry/Entity Type

Industry

Colors

Designer to choose colors to be used in the design.

Requirements
Must have
• At least 1 item we sell

```html
<!DOCTYPE html>
<html lang="en">
<head>
<meta charset="utf-8">
<title>Brightwell Spraytek Systems – Magazine Ad</title>
<link href="https://fonts.googleapis.com/css2?family=Lato:wght@300;400;700;900&display=swap" rel="stylesheet">
<style>
:root{
  --page-bg:#e6e6e6;
  --paper:#ffffff;
  --paper-fade:#ececec;
  --brand-blue:#1a7ff0;
  --ink:#2b2b2b;
  --ink-soft:#444444;
  --muted:#666666;
  --footer:#2d2d2d;
  --footer-text:#ffffff;
  --photo-teal:#3b8fa3;
  --photo-gold:#c9c48d;
  --product-bronze:#8a7a68;
}
*{box-sizing:border-box;margin:0;padding:0}
html,body{width:1200px;height:1200px;overflow:hidden;background:var(--page-bg)}
body{font-family:"Lato",sans-serif;color:var(--ink);position:relative}
.ad{
  position:absolute;left:186px;top:20px;width:907px;height:1271px;
  transform:scale(0.9127);transform-origin:top left;
  background:linear-gradient(180deg,var(--paper) 0%,var(--paper) 55%,var(--paper-fade) 100%);
  overflow:hidden;box-shadow:0 4px 14px rgba(0,0,0,.18);
}
.hero{position:absolute;left:0;top:0;width:907px;height:620px}
.headline{position:absolute;left:0;top:578px;width:907px;text-align:center;line-height:1}
.headline .lead{display:block;font-weight:300;font-size:70px;letter-spacing:-1px;color:var(--ink);margin-left:-10px}
.headline .emph{display:block;font-weight:900;font-size:92px;letter-spacing:-2px;color:var(--brand-blue);margin-top:10px;margin-left:-2px}
.beliefs{position:absolute;left:73px;top:786px;display:flex;align-items:center;font-size:17px;color:var(--ink-soft)}
.rule{display:inline-block;height:1px;background:#999;margin:0 14px 0 6px}
.belief{display:flex;align-items:center;margin-right:14px;font-size:18px}
.belief svg{margin-right:10px}
.body-copy{position:absolute;left:72px;top:836px;font-size:17px;color:var(--ink-soft)}
.products-intro{position:absolute;left:72px;top:877px;font-size:17px;color:var(--ink-soft);display:flex;align-items:center}
.products-list{position:absolute;left:71px;top:908px;font-size:17px;font-weight:700;color:var(--ink)}
.products-list span+span{margin-left:18px}
.product-photo{position:absolute;left:55px;top:978px;width:380px;height:135px;border-radius:40px;
  background:radial-gradient(ellipse at center,#b0a290 0%,var(--product-bronze) 55%,rgba(138,122,104,0) 75%)}
.range-title{position:absolute;left:496px;top:978px;font-size:38px;font-weight:700;color:var(--ink);letter-spacing:-.5px}
.range-list{position:absolute;top:1038px;list-style:none;font-size:14px;color:var(--muted);line-height:22.5px}
.range-list li::before{content:"";display:inline-block;width:5px;height:5px;border-radius:50%;background:var(--brand-blue);margin:0 10px 2px 0;vertical-align:middle}
.range-list.col-a{left:484px}
.range-list.col-b{left:670px}
.footer{position:absolute;left:0;top:1149px;width:907px;height:107px;background:var(--footer);color:var(--footer-text)}
.brand{position:absolute;left:80px;top:40px;display:flex;align-items:center;font-size:17px;font-weight:700}
.brand .dot{width:14px;height:14px;border-radius:50%;background:var(--brand-blue);margin-right:10px}
.contact{position:absolute;right:92px;top:12px;text-align:right}
.contact .phone{font-size:36px;font-weight:700;letter-spacing:.5px;line-height:40px}
.contact .line{font-size:16px;line-height:22px;display:flex;align-items:center;justify-content:flex-end}
.contact .line svg{margin-right:7px}
</style>
</head>
<body>
<main class="ad">
  <svg class="hero" viewBox="0 0 907 620" aria-hidden="false">
    <defs>
      <linearGradient id="photoTone" x1="0" y1="0" x2="1" y2="1">
        <stop offset="0" stop-color="#d8cf93"/>
        <stop offset=".4" stop-color="#7fb3b4"/>
        <stop offset=".75" stop-color="#2f7f97"/>
        <stop offset="1" stop-color="#1c4d62"/>
      </linearGradient>
    </defs>
    <path role="img" aria-label="Close-up photo of a machined steel part on a lathe" fill="url(#photoTone)"
      d="M0 0 H860 L660 215 L470 410 Q380 515 270 515 Q150 510 0 370 Z"/>
    <path d="M0 380 Q140 540 290 545 Q400 545 470 428 L525 482 Q555 505 588 472 L688 372 Q715 340 688 308 L655 268 L718 278 Q742 286 768 262 L848 182 Q872 156 848 130 L815 95 L907 3"
      fill="none" stroke="var(--brand-blue)" stroke-width="8" stroke-linejoin="round" stroke-linecap="round"/>
    <rect x="451" y="244" width="190" height="190" rx="42" fill="#fff" transform="rotate(45 546 339)"/>
    <rect role="img" aria-label="Row of nozzle fittings" x="430" y="295" width="235" height="75" rx="30" fill="var(--product-bronze)" opacity=".85"/>
    <rect x="654" y="67" width="174" height="174" rx="40" fill="#fff" transform="rotate(45 741 154)"/>
    <rect role="img" aria-label="Coiled high pressure hose" x="650" y="122" width="170" height="60" rx="28" fill="#3a3a3a"/>
  </svg>

  <h1 class="headline"><span class="lead">OUR CUSTOMER</span><span class="emph">COME FIRST</span></h1>

  <div class="beliefs">
    <span>We believe in</span><span class="rule" style="width:98px"></span>
    <span class="belief">
      <svg width="34" height="34" viewBox="0 0 34 34"><circle cx="17" cy="17" r="17" fill="var(--brand-blue)"/><rect x="10" y="9" width="14" height="10" rx="2" fill="#fff"/><circle cx="17" cy="23" r="3" fill="#fff"/><path d="M11 28 Q17 22 23 28" stroke="#fff" stroke-width="2" fill="none"/></svg>
      Customer Service</span>
    <span class="belief">
      <svg width="34" height="34" viewBox="0 0 34 34"><circle cx="17" cy="17" r="17" fill="var(--brand-blue)"/><circle cx="17" cy="10" r="3" fill="#fff"/><path d="M9 22 V17 H25 V22 M17 13 V17" stroke="#fff" stroke-width="2" fill="none"/><circle cx="9" cy="24" r="2.6" fill="#fff"/><circle cx="17" cy="24" r="2.6" fill="#fff"/><circle cx="25" cy="24" r="2.6" fill="#fff"/></svg>
      Building Relationships</span>
  </div>

  <p class="body-copy">with our customers and going above and beyond to meet our customer needs.</p>
  <p class="products-intro">Our main products we sell are our<span class="rule" style="width:98px;margin-left:8px"></span></p>
  <p class="products-list"><span>1.Quillstone Nozzles</span><span>2. Dorvane Mellick Hoses</span></p>

  <div class="product-photo" role="img" aria-label="Group of quillstone nozzle fittings"></div>
  <h2 class="range-title">Quillstone Nozzles</h2>
  <ul class="range-list col-a">
    <li>1/4” Quillstone Nozzle</li>
    <li>3/8” Quillstone Nozzle</li>
    <li>5/16” Quillstone Nozzle</li>
  </ul>
  <ul class="range-list col-b">
    <li>7/16” Quillstone Nozzle</li>
    <li>Bi-Mode Quillstone Nozzle</li>
    <li>M10 Quillstone Nozzle</li>
  </ul>

  <footer class="footer">
    <div class="brand"><span class="dot"></span>Brightwell Spraytek Systems, Inc.</div>
    <div class="contact">
      <div class="phone">555-014-2290</div>
      <div class="line"><svg width="12" height="12" viewBox="0 0 12 12"><circle cx="6" cy="6" r="5" fill="none" stroke="#fff" stroke-width="1.4"/><path d="M1 6 H11 M6 1 Q3 6 6 11 Q9 6 6 1" stroke="#fff" fill="none"/></svg>www.brightwellspraytek.example</div>
      <div class="line"><svg width="12" height="10" viewBox="0 0 12 10"><rect x="1" y="1" width="10" height="8" fill="none" stroke="#fff" stroke-width="1.4"/><path d="M1 1 L6 6 L11 1" stroke="#fff" fill="none"/></svg>info@brightwellspraytek.example</div>
    </div>
  </footer>
</main>
</body>
</html>
```